Brisk Hollow Builders Needs A Flyer

We need a flyer for our newest product "The Cedarlane Garden Workroom"

Here is some copy for the flyer:

1. More and more people everyday are working from home and finding it difficult to disconnect from home activities in order to focus on their work. They are also finding it very expensive to add on to their existing house for a quiet place. Our archatectually stunning, Cedarlane Garden Workroom is the answer. The office studio measures 16' wide and 10' deep. 160 Square feet of space.

Perfect for dozens of purposes. Home office, design studio, artist studio, home school office, reading room, craft studio, drafting room.

Features include:

- Steel Framing. 40-60% lighter then wood, higher strength to weight ratio, resistant to mold and fire and steel is the most recycled material on earth!
- Spray foam insulation. Cool in the summer and warm in the winter.
- HVAC Mini Split with wireless remote control and thermostat.
- 100% Off grid with enough solar and battery storage to run your entire office. No need to pay for an expensive electric installation.
- Flush fitting floor outlets to reduce wires.
- TV mount (Optional with pre-wired electric, HDMI, digital audio & Cat 6)
- Windows are tempered glass custom made by Morvik Glazing.
- Solar qualifies for a 26% tax credit. This is not a write-off rather it is a direct reduction on your tax obligation.
- Thousands of dollars less than adding onto your home.
- Custom color, siding, features available.

This beautiful back yard office is delivered 100% assembled and ready to enjoy on the day of delivery.

We ship nationwide from our factory in South Carolina. Give us a call anytime to speak to a designer and start your dream office today!

555-318-4027
info@BriskHollowBuilders.example

```html
<!DOCTYPE html>
<html lang="en">
<head>
<meta charset="utf-8">
<title>Brisk Hollow Builders – The Cedarlane Garden Workroom</title>
<link rel="stylesheet" href="https://fonts.googleapis.com/css2?family=Oswald:wght@500;600&family=Montserrat:wght@500;600;700&display=swap">
<style>
:root{
  --green:#5fa446;
  --orange:#f7a21b;
  --ink:#1d1d1b;
  --text:#2b2b2b;
  --panel:#e9e9e9;
  --dark:#3d3d3d;
  --backdrop:#d8d8d8;
  --white:#ffffff;
}
*{margin:0;padding:0;box-sizing:border-box}
html,body{width:1200px;height:2727px;overflow:hidden;background:var(--backdrop)}
.flyer{position:absolute;left:0;top:543px;width:1200px;height:1640px;background:var(--white);overflow:hidden;font-family:'Montserrat',sans-serif;color:var(--text)}
.header-art{position:absolute;left:0;top:0}
.brand{position:absolute;left:100px;top:100px;display:flex;align-items:center;gap:14px}
.brand-dot{width:38px;height:38px;border-radius:50%;background:var(--green)}
.brand-name{font-family:'Montserrat',sans-serif;font-weight:700;font-size:27px;color:var(--green);line-height:1.1;width:220px}
.headline{position:absolute;left:68px;top:255px;font-family:'Oswald',sans-serif;line-height:.95}
.headline .line1{display:block;font-size:80px;font-weight:500;color:var(--ink);letter-spacing:1px}
.headline .line2{display:block;font-size:80px;font-weight:600;color:var(--ink);letter-spacing:1px}
.headline .line3{display:block;font-size:54px;font-weight:600;color:var(--white);margin-top:8px;letter-spacing:.5px}
.intro{position:absolute;left:64px;top:580px;width:1018px;font-size:19.5px;font-weight:500;line-height:1.2;text-align:justify;text-align-last:center;color:var(--text)}
.features-tab{position:absolute;left:350px;top:707px;width:448px;height:54px;background:var(--orange);border-radius:28px 28px 0 0;color:var(--white);font-family:'Oswald',sans-serif;font-weight:500;font-size:38px;text-align:center;line-height:56px;letter-spacing:.5px}
.features{position:absolute;left:74px;top:762px;width:1035px;height:348px;border:2px solid var(--dark);border-radius:16px;display:flex;padding:28px 30px 0 40px}
.features ul{list-style:none;width:50%}
.features ul.right{border-left:2px solid var(--dark);padding-left:62px;margin-top:18px;height:265px;padding-top:0}
.features ul.left{padding-right:30px}
.features li{position:relative;padding-left:38px;font-size:14.5px;font-weight:600;line-height:1.28;color:var(--ink);margin-bottom:20px}
.features li svg{position:absolute;left:0;top:0}
.delivery{position:absolute;left:77px;top:1128px;width:1021px;height:366px;background:var(--panel)}
.delivery-title{position:absolute;left:0;width:100%;top:30px;text-align:center;font-size:13.5px;font-weight:700;color:var(--ink);white-space:nowrap;letter-spacing:-.1px}
.delivery-title b{color:var(--green);font-size:23px;font-weight:700}
.product{position:absolute;top:105px;height:185px}
.ship-line{position:absolute;left:0;width:100%;top:306px;text-align:center;font-size:25px;font-weight:600;color:var(--ink)}
.ship-line span{color:var(--orange)}
.cta{position:absolute;left:82px;top:1526px;width:1004px;height:42px;background:var(--green);border-radius:14px 14px 0 0;color:var(--white);font-size:19.5px;font-weight:600;text-align:center;line-height:44px;white-space:nowrap;letter-spacing:-.1px}
.footer{position:absolute;left:0;top:1567px;width:1200px;height:73px}
.footer-bg{position:absolute;left:0;top:0}
.phone{position:absolute;left:90px;top:0;height:73px;display:flex;align-items:center;gap:26px;font-family:'Montserrat',sans-serif;font-weight:700;font-size:38px;color:var(--ink)}
.contacts{position:absolute;left:475px;top:0;height:73px;display:flex;align-items:center;gap:14px;font-size:17px;font-weight:500;color:var(--white);white-space:nowrap}
.contacts .item{display:flex;align-items:center;gap:9px}
</style>
</head>
<body>
<main class="flyer">
  <svg class="header-art" width="1200" height="531" viewBox="0 0 1200 531">
    <defs>
      <linearGradient id="photoTone" x1="0" y1="0" x2="1" y2="1">
        <stop offset="0" stop-color="#9bbcd6"/>
        <stop offset=".35" stop-color="#6f7c62"/>
        <stop offset=".7" stop-color="#4b4f4c"/>
        <stop offset="1" stop-color="#8a8470"/>
      </linearGradient>
    </defs>
    <rect x="0" y="232" width="1200" height="299" fill="var(--green)"/>
    <path d="M590,0 L1200,0 L1200,531 L1080,531 C880,540 700,470 610,330 C545,230 545,80 590,0 Z" fill="var(--white)"/>
    <path d="M606,0 L1200,0 L1200,505 C1000,545 740,480 640,340 C570,240 565,90 606,0 Z" fill="url(#photoTone)" role="img" aria-label="Photo of the modern garden workroom with dark steel frame, glass walls and a furnished interior, set in a leafy back yard"/>
  </svg>

  <div class="brand">
    <span class="brand-dot"></span>
    <span class="brand-name">Brisk Hollow Builders</span>
  </div>

  <h1 class="headline">
    <span class="line1">THE CEDARLANE</span>
    <span class="line2">GARDEN</span>
    <span class="line3">WORKROOM</span>
  </h1>

  <p class="intro">More and more people everyday are working from home and finding it difficult to disconnect from home activities in order to focus on their work. They are also finding it very expensive to add on to their existing house for a quiet place. Our archatectually stunning, Cedarlane Garden Workroom is the answer. The office studio measures 16' wide and 10' deep. 160 Square feet of space.</p>

  <div class="features-tab">FEATURES INCLUDE:</div>
  <section class="features">
    <ul class="left">
      <li><svg width="18" height="18" viewBox="0 0 18 18"><circle cx="9" cy="9" r="7.5" fill="none" stroke="var(--orange)" stroke-width="1.6"/><path d="M5.5,9.2 L8,11.5 L12.5,6.8" fill="none" stroke="var(--orange)" stroke-width="1.6"/></svg>Steel Framing. 40-60% lighter then wood, higher strength to weight ratio, resistant to mold and fire and steel is the most recycled material on earth!</li>
      <li><svg width="18" height="18" viewBox="0 0 18 18"><circle cx="9" cy="9" r="7.5" fill="none" stroke="var(--orange)" stroke-width="1.6"/><path d="M5.5,9.2 L8,11.5 L12.5,6.8" fill="none" stroke="var(--orange)" stroke-width="1.6"/></svg>Spray foam insulation. Cool in the summer and warm in the winter.</li>
      <li><svg width="18" height="18" viewBox="0 0 18 18"><circle cx="9" cy="9" r="7.5" fill="none" stroke="var(--orange)" stroke-width="1.6"/><path d="M5.5,9.2 L8,11.5 L12.5,6.8" fill="none" stroke="var(--orange)" stroke-width="1.6"/></svg>HVAC Mini Split with wireless remote control and thermostat.</li>
      <li><svg width="18" height="18" viewBox="0 0 18 18"><circle cx="9" cy="9" r="7.5" fill="none" stroke="var(--orange)" stroke-width="1.6"/><path d="M5.5,9.2 L8,11.5 L12.5,6.8" fill="none" stroke="var(--orange)" stroke-width="1.6"/></svg>100% Off grid with enough solar and battery storage to run your entire office. No need to pay for an expensive electric installation.</li>
      <li><svg width="18" height="18" viewBox="0 0 18 18"><circle cx="9" cy="9" r="7.5" fill="none" stroke="var(--orange)" stroke-width="1.6"/><path d="M5.5,9.2 L8,11.5 L12.5,6.8" fill="none" stroke="var(--orange)" stroke-width="1.6"/></svg>Flush fitting floor outlets to reduce wires.</li>
    </ul>
    <ul class="right">
      <li><svg width="18" height="18" viewBox="0 0 18 18"><circle cx="9" cy="9" r="7.5" fill="none" stroke="var(--orange)" stroke-width="1.6"/><path d="M5.5,9.2 L8,11.5 L12.5,6.8" fill="none" stroke="var(--orange)" stroke-width="1.6"/></svg>TV mount (Optional with pre-wired electric, HDMI, digital audio &amp; Cat 6)</li>
      <li><svg width="18" height="18" viewBox="0 0 18 18"><circle cx="9" cy="9" r="7.5" fill="none" stroke="var(--orange)" stroke-width="1.6"/><path d="M5.5,9.2 L8,11.5 L12.5,6.8" fill="none" stroke="var(--orange)" stroke-width="1.6"/></svg>Windows are tempered glass custom made by Morvik Glazing.</li>
      <li><svg width="18" height="18" viewBox="0 0 18 18"><circle cx="9" cy="9" r="7.5" fill="none" stroke="var(--orange)" stroke-width="1.6"/><path d="M5.5,9.2 L8,11.5 L12.5,6.8" fill="none" stroke="var(--orange)" stroke-width="1.6"/></svg>Solar qualifies for a 26% tax credit. This is not a write-off rather it is a direct reduction on your tax obligation.</li>
      <li><svg width="18" height="18" viewBox="0 0 18 18"><circle cx="9" cy="9" r="7.5" fill="none" stroke="var(--orange)" stroke-width="1.6"/><path d="M5.5,9.2 L8,11.5 L12.5,6.8" fill="none" stroke="var(--orange)" stroke-width="1.6"/></svg>Thousands of dollars less than adding onto your home.</li>
      <li><svg width="18" height="18" viewBox="0 0 18 18"><circle cx="9" cy="9" r="7.5" fill="none" stroke="var(--orange)" stroke-width="1.6"/><path d="M5.5,9.2 L8,11.5 L12.5,6.8" fill="none" stroke="var(--orange)" stroke-width="1.6"/></svg>Custom color, siding, features available.</li>
    </ul>
  </section>

  <section class="delivery">
    <p class="delivery-title">THIS BEAUTIFUL BACK YARD OFFICE IS DELIVERED <b>100%</b> ASSEMBLED AND READY TO ENJOY ON THE DAY OF DELIVERY.</p>
    <svg class="product" style="left:28px" width="312" height="185" viewBox="0 0 312 185" role="img" aria-label="Workroom shown from the left corner"><defs><linearGradient id="unitTone" x1="0" y1="0" x2="0" y2="1"><stop offset="0" stop-color="#3a3a3a"/><stop offset=".5" stop-color="#bdb5a8"/><stop offset="1" stop-color="#4a4a4a"/></linearGradient></defs><rect x="10" y="10" width="292" height="165" fill="url(#unitTone)"/></svg>
    <svg class="product" style="left:360px" width="290" height="185" viewBox="0 0 290 185" role="img" aria-label="Workroom shown from the front"><rect x="5" y="10" width="280" height="165" fill="url(#unitTone)"/></svg>
    <svg class="product" style="left:672px" width="320" height="185" viewBox="0 0 320 185" role="img" aria-label="Workroom shown from the right corner"><rect x="10" y="10" width="300" height="165" fill="url(#unitTone)"/></svg>
    <p class="ship-line">We ship nationwide from our factory in <span>South Carolina.</span></p>
  </section>

  <div class="cta">Give us a call anytime to speak to a designer and start your dream office today!</div>

  <footer class="footer">
    <svg class="footer-bg" width="1200" height="73" viewBox="0 0 1200 73">
      <rect width="1200" height="73" fill="var(--dark)"/>
      <polygon points="0,0 446,0 470,73 0,73" fill="var(--orange)"/>
      <polygon points="446,0 454,0 478,73 470,73" fill="var(--white)"/>
    </svg>
    <div class="phone">
      <svg width="26" height="26" viewBox="0 0 24 24"><path d="M6.6,2.5 L9.5,6.8 L7.6,9 C8.8,11.6 11.4,14.2 14,15.4 L16.2,13.5 L20.5,16.4 L18.6,20.3 C11,20 3.8,12.8 3,5 Z" fill="var(--ink)"/></svg>
      <span>555-318-4027</span>
    </div>
    <div class="contacts">
      <span class="item"><svg width="16" height="16" viewBox="0 0 16 16"><rect x="1" y="3" width="14" height="10" rx="1.5" fill="var(--orange)"/><path d="M1.5,4 L8,9 L14.5,4" fill="none" stroke="var(--dark)" stroke-width="1.3"/></svg>info@BriskHollowBuilders.example</span>
      <span class="item"><svg width="16" height="16" viewBox="0 0 16 16"><circle cx="8" cy="8" r="7" fill="var(--orange)"/><path d="M1,8 H15 M8,1 C4,5 4,11 8,15 M8,1 C12,5 12,11 8,15" fill="none" stroke="var(--dark)" stroke-width="1.1"/></svg>www.briskhollowbuilders.example</span>
    </div>
  </footer>
</main>
</body>
</html>
```